Custom MS Teams backgrounds for VOLUMN

Want to create a set of custom backgrounds to use in MS Teams video calls for our IT / Digital Consultancy company. The intention is to use if for internal video calls and also when communicating with clients.

Our employees are in the ages 25 years and up, men and women.

Our clients are in high tech, automative and Medical device space mainly.

Images should include the VOLUMN logo and give a professional impression, and some wow factor.

Target Market(s)

For business use.

Industry/Entity Type

It Company

Requirements
Must have
• Crisp images to use as backgrounds for MS Teams
images includes the VOLUMN logo.

At least three different images, at least one should be an office space and one should be a high-tech/digital image (e.g., automotive, Medical Tech etc, space etc.)

The logo should be part of the image, example, if the image is a Brooklyn office space, then it should look like the VOLUMN logo is on the back wall as if it was there IRL. Its
Nice to have
• Futuristic pictures of high-tech labs or high-tech equipment with the logo naturally placed on the main item in the picture.

Office space pictures, "cool" contemporary offices. Logo placed on back wall.

Logo can also be converted to monochrome, i.e., white / black / glass / light etc. or 3D rendered to stand out from example a wall surface.

Innovation is welcome i.e., superimposing the logo on the Qasr Tamiyah so it looks like an VOLUMN lightshow or something completely different.
Should not have
• Should not have People in the pictures.

Not weapons or arms industry.

Have in mind that in MS Teams the person on the call covers the center of the picture so the placement of the logo and features that should be shown need to take this into account.

```html
<!DOCTYPE html>
<html lang="en">
<head>
<meta charset="utf-8">
<title>VOLUMN – 3 Concept Design</title>
<link rel="stylesheet" href="https://fonts.googleapis.com/css2?family=Montserrat:wght@400;500;600;700&family=Lato:wght@400&display=swap">
<style>
  :root {
    --page-bg: #ffffff;
    --title-grey: #4a4a4a;
    --logo-cyan: #1fa9e6;
    --logo-charcoal: #2b2b30;
    --logo-light: #e4e8ee;
    --mission-blue: #1f8fd6;
    --mission-text: #3f7fd0;
    --night-deep: #02040a;
    --night-blue: #0c2a5c;
    --star-gold: #f6c94a;
    --rose-core: #fff1f4;
    --rose-mid: #e8406c;
    --rose-edge: #5e1d45;
    --city-sky: #22466c;
    --city-dusk: #c06a72;
    --city-ground: #0b1020;
    --city-glow: #d8953c;
    --city-violet: #8a3fa8;
  }
  * { margin: 0; padding: 0; box-sizing: border-box; }
  html, body { width: 800px; height: 1200px; overflow: hidden; background: var(--page-bg); }
  body { position: relative; font-family: "Montserrat", Arial, sans-serif; }

  .sheet-title {
    position: absolute; top: 36px; left: 0; width: 800px;
    text-align: center; font-weight: 500; font-size: 22px;
    letter-spacing: 1px; color: var(--title-grey);
  }

  .concept { position: absolute; left: 106px; width: 587px; overflow: hidden; }
  .concept--stars { top: 93px; height: 349px; }
  .concept--tunnel { top: 494px; height: 291px; }
  .concept--city { top: 850px; height: 244px; }

  .backdrop { position: absolute; inset: 0; }
  .backdrop--stars {
    background:
      radial-gradient(ellipse 14% 10% at 28% 22%, rgba(246,201,74,.45), transparent 70%),
      radial-gradient(ellipse 12% 9% at 74% 20%, rgba(246,201,74,.4), transparent 70%),
      radial-gradient(ellipse 10% 9% at 10% 45%, rgba(246,201,74,.35), transparent 70%),
      radial-gradient(ellipse 10% 9% at 92% 40%, rgba(246,201,74,.35), transparent 70%),
      radial-gradient(ellipse 90% 38% at 50% 6%, rgba(246,201,74,.18), transparent 70%),
      radial-gradient(ellipse 30% 30% at 12% 18%, rgba(60,120,210,.6), transparent 70%),
      radial-gradient(ellipse 30% 30% at 88% 18%, rgba(60,120,210,.6), transparent 70%),
      linear-gradient(180deg, var(--night-blue) 0%, #081c42 40%, #041026 70%, var(--night-deep) 100%);
  }
  .backdrop--tunnel {
    background:
      radial-gradient(ellipse 55% 28% at 62% 30%, rgba(255,214,120,.35), transparent 70%),
      radial-gradient(ellipse 40% 60% at 88% 30%, rgba(70,40,110,.7), transparent 70%),
      radial-gradient(ellipse 50% 40% at 80% 95%, rgba(255,40,80,.55), transparent 70%),
      radial-gradient(circle at 27% 50%, var(--rose-core) 0%, #f9b9c8 14%, #ef6b8d 32%, var(--rose-mid) 50%, #a72b5a 75%, var(--rose-edge) 100%);
  }
  .backdrop--city {
    background:
      radial-gradient(ellipse 40% 30% at 50% 72%, rgba(216,149,60,.45), transparent 70%),
      radial-gradient(ellipse 30% 25% at 80% 85%, rgba(138,63,168,.45), transparent 70%),
      radial-gradient(ellipse 30% 25% at 20% 88%, rgba(216,149,60,.35), transparent 70%),
      radial-gradient(ellipse 35% 14% at 10% 40%, rgba(220,120,120,.7), transparent 70%),
      linear-gradient(180deg, var(--city-sky) 0%, #2f4d70 28%, #6a5c78 40%, #2c3650 52%, #151c30 70%, var(--city-ground) 100%);
  }

  .brand-name {
    position: absolute; font-family: "Montserrat", Arial, sans-serif;
    font-weight: 600; letter-spacing: 1px; line-height: 1; white-space: nowrap;
  }
  .concept--stars .brand-name { left: 306px; top: 181px; transform: translateX(-50%); font-size: 42px; color: var(--logo-cyan); }
  .concept--tunnel .brand-name { left: 48px; top: 142px; font-size: 34px; color: var(--logo-charcoal); }
  .concept--city .brand-name { left: 300px; top: 30px; transform: translateX(-50%); font-size: 34px; color: var(--logo-light); }

  .mission {
    position: absolute; left: 50%; top: 250px; transform: translateX(-50%);
    width: 492px; text-align: center;
  }
  .mission__heading {
    font-family: "Montserrat", Arial, sans-serif; font-weight: 500;
    font-size: 10.5px; letter-spacing: .8px; color: var(--mission-blue);
    margin-bottom: 3px;
  }
  .mission__body {
    font-family: "Lato", Arial, sans-serif; font-size: 6.6px;
    line-height: 8.4px; color: var(--mission-text);
  }
</style>
</head>
<body>
  <h1 class="sheet-title">3 CONCEPT DESIGN</h1>

  <section class="concept concept--stars">
    <div class="backdrop backdrop--stars" role="img" aria-label="Deep blue night sky with glowing golden stars arching across the top"></div>
    <div class="brand-name">VOLUMN</div>
    <div class="mission">
      <h2 class="mission__heading">MISSION STATEMENT</h2>
      <p class="mission__body">We build digital products that move industries forward. Our teams pair engineering depth with clear thinking to help partners in high tech, automotive and medical devices ship reliable software. We listen first, design with care and deliver with precision. Every project is measured by the value it creates for the people who rely on it. We grow through trust, curiosity and shared ambition, and we stay close to our clients from the first idea to the final release and beyond. We invest in our people, share what we learn and keep raising the standard of our craft so that every partner can build with confidence today and tomorrow.</p>
    </div>
  </section>

  <section class="concept concept--tunnel">
    <div class="backdrop backdrop--tunnel" role="img" aria-label="Swirling pink and magenta tunnel of glowing light dots around a bright white centre"></div>
    <div class="brand-name">VOLUMN</div>
  </section>

  <section class="concept concept--city">
    <div class="backdrop backdrop--city" role="img" aria-label="Aerial night city skyline at dusk with vertical light beams and glowing light trails"></div>
    <div class="brand-name">VOLUMN</div>
  </section>
</body>
</html>
```